Business card design needed for rebranded top-end landscaping business

We need a new business card design, incorporating our logo (colours Green #8dc63f and Grey #8a8c8e) and also some options that include the colour dark navy (eg #000040) as our uniforms are navy with white and grey trim.

We are an innovative landscaping company that maintains high-end gardens for meticulous clients. We pride ourselves on our customer service, our professionalism, and our workmanship.

Our business name needs to be easily read and our branding needs to be bold and memorable, without screaming "tradesman"! We prefer clean lines over lots of fine detail.

The design MUST include:
- Business name ("Brambleton Gardenworks")
- Logo (file uploaded)
- Employee name
- Phone number
- Email address
- www.brambletongardenworks.com.au
- Friendspace & Snapgrid logos
- The Turfcraft Guild logo (file uploaded) along with the word "Member"
- Licence "Lic. 618392K"

OPTIONAL inclusions:
- "Creating outdoor spaces for our community to be inspired, refreshed and re-energised"
- "Landscape Maintenance - Irrigation - Arboriculture" (dashes can be replaced with dots or other)
- "Fully qualified, licensed & insured"
- "Residential - Strata - Commercial - Real Estate" (dashes can be replaced with dots or other)

High-end professionals and retirees, real estate agents

Landscaping

See Project description

Sans Serif

Designer to choose colors to be used in the design.

• Must incorporate our logo, and colours Green #8dc63f and Grey #8a8c8e) from the logo, and the colour DARK NAVY (eg #000040).
• The design MUST include:
• - Business name ("Brambleton Gardenworks")
• - Logo (file uploaded)
• - Employee name
• - Phone number
• - Email address
• - www.brambletongardenworks.com.au
• - Friendspace & Snapgrid logos
• - The Turfcraft Guild logo (file uploaded) along with the word "Member"
• - Licence "Lic. 618392K"
• OPTIONAL inclusions:
• - "Creating outdoor spaces for our community to be inspired, refreshed and re-energised"
• - "Landscape Maintenance - Irrigation - Arboriculture" (dashes can be replaced with dots or other)
• - "Fully qualified, licensed & insured"
• - "Residential - Strata - Commercial - Real Estate" (dashes can be replaced with dots or other)

```html
<!DOCTYPE html>
<html lang="en">
<head>
<meta charset="utf-8">
<title>Brambleton Gardenworks — Business Cards</title>
<link rel="stylesheet" href="https://fonts.googleapis.com/css2?family=Quicksand:wght@500;600;700&display=swap">
<style>
  :root {
    --navy: #1b1a52;
    --navy-edge: #0e0d38;
    --green: #8dc63f;
    --grey: #8a8c8e;
    --grey-light: #a9abad;
    --page: #e9e8e4;
  }
  * { box-sizing: border-box; margin: 0; padding: 0; }
  html, body { width: 960px; height: 1200px; overflow: hidden; }
  body {
    background: var(--page);
    font-family: "Quicksand", sans-serif;
    position: relative;
  }
  .card {
    position: absolute;
    left: 60px;
    width: 840px;
    height: 477px;
    background: var(--navy);
    border: 4px solid var(--navy-edge);
    overflow: hidden;
  }
  .card--brand { top: 90px; }
  .card--contact { top: 633px; }

  /* Brand side */
  .brand-mark {
    position: absolute;
    left: 50%;
    top: 40px;
    width: 92px;
    height: 92px;
    margin-left: -46px;
    border-radius: 50%;
    background: var(--green);
  }
  .brand-name {
    position: absolute;
    left: 0; right: 0;
    top: 160px;
    text-align: center;
    color: var(--grey);
    font-weight: 700;
    font-size: 50px;
    letter-spacing: 0.5px;
  }
  .band-thin {
    position: absolute;
    left: 8px; right: 8px;
    top: 290px;
    height: 28px;
    background: var(--green);
  }
  .licence {
    position: absolute;
    left: 110px;
    top: 324px;
    color: var(--green);
    font-size: 25px;
    font-weight: 600;
    letter-spacing: 2px;
  }
  .band-social {
    position: absolute;
    left: 8px; right: 8px;
    top: 364px;
    height: 102px;
    background: var(--green);
  }
  .social {
    position: absolute;
    top: 396px;
    display: flex;
    align-items: center;
    gap: 20px;
    color: var(--navy);
    font-size: 25px;
    font-weight: 600;
    letter-spacing: 2px;
  }
  .social--one { left: 44px; }
  .social--two { left: 356px; }
  .social-icon { width: 38px; height: 38px; flex: none; }
  .social-icon--square { background: var(--grey); border-radius: 3px; }
  .social-icon--circle { border: 4px solid var(--grey); border-radius: 50%; }

  .member-badge {
    position: absolute;
    left: 596px;
    top: 300px;
    width: 228px;
    height: 156px;
    background: var(--grey-light);
  }
  .member-label {
    position: absolute;
    left: 0; right: 0;
    top: 10px;
    text-align: center;
    color: var(--navy);
    font-size: 24px;
    font-weight: 600;
    letter-spacing: 2px;
  }
  .guild-mark {
    position: absolute;
    left: 34px;
    top: 56px;
    width: 160px;
    height: 80px;
    background: var(--grey);
  }

  /* Contact side */
  .header-band {
    position: absolute;
    left: 8px; right: 8px;
    top: 12px;
    height: 64px;
    background: var(--green);
    color: var(--navy);
    font-weight: 700;
    font-size: 32px;
    letter-spacing: 1px;
    text-align: center;
    line-height: 64px;
  }
  .contact-mark {
    position: absolute;
    left: 172px;
    top: 112px;
    width: 60px;
    height: 60px;
    border-radius: 50%;
    background: var(--green);
  }
  .contact-name {
    position: absolute;
    left: 62px;
    width: 280px;
    top: 186px;
    text-align: center;
    color: var(--grey);
    font-weight: 700;
    font-size: 28px;
    line-height: 1.15;
  }
  .divider-vertical {
    position: absolute;
    left: 380px;
    top: 92px;
    width: 3px;
    height: 180px;
    background: var(--grey);
  }
  .employee-name {
    position: absolute;
    left: 384px; right: 0;
    top: 164px;
    text-align: center;
    color: var(--green);
    font-size: 34px;
    font-weight: 600;
    letter-spacing: 1px;
  }
  .contact-band {
    position: absolute;
    left: 8px; right: 8px;
    top: 288px;
    height: 178px;
    background: var(--green);
  }
  .contact-row {
    position: absolute;
    left: 40px;
    display: flex;
    align-items: center;
    height: 44px;
    color: var(--navy);
    font-size: 25px;
    font-weight: 600;
    letter-spacing: 1px;
  }
  .contact-row--phone { top: 298px; }
  .contact-row--email { top: 360px; }
  .contact-row--web { top: 418px; }
  .contact-icon { width: 44px; height: 34px; flex: none; }
  .row-rule {
    width: 3px;
    height: 40px;
    background: var(--navy);
    margin: 0 20px 0 22px;
  }
</style>
</head>
<body>

  <section class="card card--brand" aria-label="Card front">
    <div class="brand-mark"></div>
    <div class="brand-name">Brambleton Gardenworks</div>
    <div class="band-thin"></div>
    <div class="licence">LICENCE "LIC. 618392K"</div>
    <div class="band-social"></div>
    <div class="social social--one"><span class="social-icon social-icon--square"></span>FRIENDSPACE</div>
    <div class="social social--two"><span class="social-icon social-icon--circle"></span>SNAPGRID</div>
    <div class="member-badge">
      <div class="member-label">MEMBER</div>
      <div class="guild-mark" role="img" aria-label="The Turfcraft Guild member badge"></div>
    </div>
  </section>

  <section class="card card--contact" aria-label="Card back">
    <div class="header-band">BRAMBLETON GARDENWORKS</div>
    <div class="contact-mark"></div>
    <div class="contact-name">Brambleton Gardenworks</div>
    <div class="divider-vertical"></div>
    <div class="employee-name">EMPLOYEE NAME</div>
    <div class="contact-band"></div>

    <div class="contact-row contact-row--phone">
      <svg class="contact-icon" viewBox="0 0 44 34" aria-hidden="true">
        <path d="M4 12 Q22 2 40 12 L37 17 L30 15 L29 11 Q22 9 15 11 L14 15 L7 17 Z" fill="var(--navy)"/>
        <rect x="10" y="17" width="24" height="14" rx="3" fill="var(--navy)"/>
        <circle cx="22" cy="24" r="4" fill="var(--green)"/>
      </svg>
      <span class="row-rule"></span>000-000-0000
    </div>
    <div class="contact-row contact-row--email">
      <svg class="contact-icon" viewBox="0 0 44 34" aria-hidden="true">
        <rect x="6" y="6" width="32" height="22" fill="var(--navy)"/>
        <path d="M6 6 L22 19 L38 6" fill="none" stroke="var(--green)" stroke-width="2"/>
      </svg>
      <span class="row-rule"></span>INFO@BRAMBLETONGARDENWORKS.COM.AU
    </div>
    <div class="contact-row contact-row--web">
      <svg class="contact-icon" viewBox="0 0 44 34" aria-hidden="true">
        <circle cx="22" cy="17" r="14" fill="none" stroke="var(--navy)" stroke-width="3"/>
        <ellipse cx="22" cy="17" rx="6" ry="14" fill="none" stroke="var(--navy)" stroke-width="2"/>
        <line x1="8" y1="17" x2="36" y2="17" stroke="var(--navy)" stroke-width="2"/>
        <line x1="11" y1="10" x2="33" y2="10" stroke="var(--navy)" stroke-width="2"/>
        <line x1="11" y1="24" x2="33" y2="24" stroke="var(--navy)" stroke-width="2"/>
      </svg>
      <span class="row-rule"></span>WWW.BRAMBLETONGARDENWORKS.COM.AU
    </div>
  </section>

</body>
</html>
```